Lorvik.no is a new website about pedagogical entrepreneurship. It's main target group is teachers. The Fjellmark Bureau for Digital Schooling and the Halvstad Agency for Classroom Affairs are leading the project.

The web page is meant to show examples of how different methods of entrepreneurship can be used pedagogical in a learning environment. The page will also support the user with examples of different teaching programs and other examples of best practice.

Pedagogical entrepreneurship is not about business and men in suits. It's a method for learning. The focus in the design should be on school, education and new ways of learning.

The final product should be motivating and engaging, but at the same time governmental and serious. We are not looking for something "flashy" and corporate-looking, but a moderate, task-focused and clean design that state quality.

We need designs for three pages:
1 - frontpage
2 - subpage ("Metoder og undervisningsopplegg")
3 - subpage ("Tavle-KOMP i Brekkvoll")

The interaction design for these three pages will be uploaded as an attachment.

We would like you to find inspiration in the following websites:
- www.skaperlund.no
- www.guldrim.no
- www.brambelquest.com
- www.tuv.no
(more will be added)

Please use the attached logo, and feel free to use this as an inspiration for the rest of the design.

Reason: We are awaiting improved designs from some designers, and need to extend the deadline a couple of days.

Target Market(s)

Teachers

Industry/Entity Type

Education

Requirements
Must have
• * Header with: Logo. Main navigation. Utility navigation. Search box.
* Footer
Should not have
• Images of men in suits.
Very strong graphical elements that stands out too much (we want it clean).

```html
<!DOCTYPE html>
<html lang="en">
<head>
<meta charset="utf-8">
<title>Lorvik.no – Pedagogical entrepreneurship</title>
<link href="https://fonts.googleapis.com/css2?family=Open+Sans:wght@300;400;600;700&family=Arimo:wght@400;700&display=swap" rel="stylesheet">
<style>
:root{
  --navy:#164a7a;
  --blue:#1c6cb0;
  --blue-mid:#2f86c8;
  --sky:#5fb4e6;
  --pale:#d6ebf8;
  --pink:#e0007a;
  --text:#1b4f86;
  --ink:#111;
  --white:#fff;
}
*{margin:0;padding:0;box-sizing:border-box}
html,body{width:1121px;height:1200px;overflow:hidden;background:var(--white)}
.page{position:relative;width:1280px;height:1370px;transform:scale(.87578);transform-origin:0 0;
  font-family:"Arimo",Arial,sans-serif;color:var(--text);
  background:linear-gradient(180deg,#fff 0,#fff 330px,#cfe6f6 420px,#c9e3f5 980px,#9fcdec 1060px,#6fb3e2 1072px);overflow:hidden}
a{color:inherit;text-decoration:none}
.abs{position:absolute}
.topband{left:0;top:0;width:1280px;height:10px;background:linear-gradient(90deg,#164a7a,#2a7fc0 50%,#164a7a)}
.brand{left:150px;top:30px;display:flex;align-items:center;gap:14px;font-family:"Open Sans",sans-serif;font-weight:700;font-size:50px;color:var(--blue-mid);letter-spacing:-1px}
.brand .dot{width:58px;height:58px;border-radius:50%;background:var(--blue-mid)}
.util-nav{top:17px;left:598px;display:flex;gap:27px;font-size:12px;font-weight:700;color:var(--navy)}
.util-nav .current{color:var(--pink)}
.search{left:960px;top:10px;width:160px;height:30px;background:var(--blue);border-radius:0 0 4px 4px;color:#a9cdeb;font-size:12px;padding:8px 12px}
.search svg{position:absolute;right:10px;top:5px}
.hero-photo{left:470px;top:10px;width:660px;height:290px;
  background:radial-gradient(ellipse at 60% 40%,#d9c2a8 0,#e9dccd 40%,rgba(255,255,255,0) 72%)}
.hero-title{left:180px;top:148px;font-family:"Open Sans",sans-serif;font-weight:400;font-size:26px;color:var(--pink)}
.hero-sub{left:180px;top:182px;font-family:"Open Sans",sans-serif;font-weight:700;font-size:13px;color:var(--pink)}
.feature{top:285px;width:300px;height:125px}
.feature h2{position:absolute;font-family:"Open Sans",sans-serif;font-weight:400;font-size:25px;line-height:30px;color:var(--text)}
.feature .icon{position:absolute;left:0;top:5px}
.btn{position:absolute;left:0;top:100px;width:270px;height:22px;border-radius:3px;background:linear-gradient(180deg,#6cc0ee,#2f86c8);
  color:#fff;font-family:"Open Sans",sans-serif;font-weight:700;font-size:12.5px;letter-spacing:-.2px;padding:3px 9px;white-space:nowrap}
.btn.pink{background:linear-gradient(180deg,#f0409a,#d0006e)}
.btn .go{position:absolute;right:-12px;top:-4px;width:30px;height:30px;background:#fff;transform:rotate(45deg);border-radius:4px;box-shadow:0 0 0 1px #cde}
.btn .go::after{content:"";position:absolute;left:6px;top:6px;width:18px;height:18px;border-radius:50%;background:var(--navy)}
.btn.pink .go::after{background:var(--pink)}
.divider{top:310px;height:105px;border-left:1px dashed #9cc8e6}
.shadow{top:440px;width:240px;height:22px;border-radius:50%;background:rgba(120,160,200,.35);filter:blur(6px)}
.panel{background:#fff;border-radius:4px;box-shadow:0 1px 3px rgba(0,0,0,.25);overflow:hidden}
.panel-head{height:33px;background:linear-gradient(180deg,#3a8fd0,#1a5f9e);color:#fff;font-family:"Open Sans",sans-serif;font-size:21px;padding:2px 13px}
.quiz-title{font-family:"Open Sans",sans-serif;font-weight:700;font-size:21px;line-height:26px;color:var(--blue-mid)}
.quiz-text{font-size:14px;color:var(--blue-mid);line-height:18px}
.list-col h3{font-family:"Open Sans",sans-serif;font-weight:700;font-size:23px;color:var(--text);margin-bottom:4px}
.list-col li{list-style:none;font-size:16px;line-height:24px;color:var(--text)}
.list-col li.active{color:var(--pink);text-decoration:underline}
.card{position:absolute;top:44px;width:300px}
.card .thumb{position:absolute;left:0;top:2px;width:146px;height:146px;box-shadow:0 3px 5px rgba(0,0,0,.3)}
.card .body{position:absolute;left:156px;top:0;width:140px;color:var(--ink)}
.card h4{font-weight:400;font-size:16px;line-height:20px}
.card p{font-size:12px;line-height:14.5px;margin-top:6px}
.card .more{font-size:12.5px;margin-top:8px}
.pager{left:598px;top:964px;display:flex;gap:6px}
.pager span{width:17px;height:17px;border-radius:50%;background:#9ad0f0}
.pager .on{background:var(--pink);box-shadow:inset 0 0 0 3px #f4a3cf}
.arrow{top:850px;width:22px;height:52px;border-radius:4px;color:#fff;font-weight:700;font-size:20px;text-align:center;line-height:50px}
.footer{left:0;top:1077px;width:1280px;height:293px;background:var(--navy);color:#fff}
.footer .rule{position:absolute;left:0;top:86px;width:1280px;border-top:1px solid #3a7ab6}
.footer h5{position:absolute;font-family:"Open Sans",sans-serif;font-weight:400;font-size:20px;line-height:24px}
.footer ul{position:absolute;top:96px;list-style:none;font-size:12px;line-height:24px;color:#dce9f6}
.footer .hot{color:var(--pink)}
.f-brand{left:172px;top:26px;display:flex;align-items:center;gap:10px;font-family:"Open Sans",sans-serif;font-weight:700;font-size:38px;color:var(--sky)}
.f-brand .dot{width:44px;height:44px;border-radius:50%;background:var(--sky)}
.copy{left:181px;top:97px;font-size:12px;color:var(--sky)}
</style>
</head>
<body>
<div class="page">
  <div class="abs topband"></div>
  <div class="abs hero-photo" role="img" aria-label="Photo of smiling students working with laptops at a classroom table"></div>

  <a class="abs brand" href="#"><span class="dot"></span>Lorvik</a>

  <nav class="abs util-nav">
    <a class="current" href="#">Best practice schools</a>
    <a href="#">Lorvikometer</a>
    <a href="#">About lorvik.no</a>
  </nav>
  <div class="abs search">Searching for...
    <svg width="22" height="20" viewBox="0 0 22 20"><circle cx="8" cy="8" r="6" fill="none" stroke="#cfe4f6" stroke-width="2.5"/><line x1="12.5" y1="12.5" x2="20" y2="18" stroke="#cfe4f6" stroke-width="3.5" stroke-linecap="round"/></svg>
  </div>

  <h1 class="abs hero-title">Learning in new ways?</h1>
  <p class="abs hero-sub">Pedagogical entrepreneurship works.</p>

  <section class="abs feature" style="left:172px">
    <svg class="icon" width="85" height="80" viewBox="0 0 85 80"><circle cx="55" cy="35" r="30" fill="none" stroke="#2f86c8" stroke-width="4"/><circle cx="55" cy="28" r="10" fill="#2f86c8"/><path d="M38 58c2-12 32-12 34 0z" fill="#2f86c8"/><line x1="32" y1="58" x2="5" y2="78" stroke="#164a7a" stroke-width="8" stroke-linecap="round"/></svg>
    <h2 style="left:88px;top:0">What is<br>pedagogical<br>entrepreneurship?</h2>
    <a class="btn" style="left:8px;width:270px" href="#">LEARN ABOUT WHAT, WHY AND HOW!<span class="go"></span></a>
  </section>
  <div class="abs divider" style="left:482px"></div>
  <section class="abs feature" style="left:505px">
    <svg class="icon" width="90" height="85" viewBox="0 0 90 85"><g fill="none" stroke="#2f86c8" stroke-width="5"><circle cx="18" cy="65" r="11"/><circle cx="40" cy="38" r="9"/><circle cx="72" cy="15" r="11"/><line x1="25" y1="56" x2="34" y2="45"/><line x1="48" y1="34" x2="62" y2="22"/></g></svg>
    <h2 style="left:90px;top:30px">Methods and<br>teaching plans</h2>
    <a class="btn" href="#">PLAIN YOUR LESSONS!<span class="go"></span></a>
  </section>
  <div class="abs divider" style="left:806px"></div>
  <section class="abs feature" style="left:829px">
    <div class="icon" role="img" aria-label="Illustration of a green sprouting plant" style="left:10px;width:70px;height:90px;border-radius:40% 40% 10% 10%;background:linear-gradient(180deg,#7ccf3a,#1f8a2e)"></div>
    <h2 style="left:90px;top:30px;color:var(--pink)">Good examples,<br>best practice</h2>
    <a class="btn pink" href="#">BE INSPIRED!<span class="go"></span></a>
  </section>
  <div class="abs shadow" style="left:190px"></div>
  <div class="abs shadow" style="left:515px"></div>
  <div class="abs shadow" style="left:840px"></div>

  <section class="abs panel" style="left:170px;top:518px;width:300px;height:205px">
    <div class="panel-head">Test youself!</div>
    <svg class="abs" style="left:18px;top:60px" width="74" height="104" viewBox="0 0 74 104"><rect x="10" y="16" width="54" height="54" rx="8" transform="rotate(45 37 43)" fill="none" stroke="#2f86c8" stroke-width="4"/><rect x="23" y="29" width="28" height="28" fill="none" stroke="#2f86c8" stroke-width="3" stroke-dasharray="5 3"/><path d="M26 42l9 10 20-22" fill="none" stroke="#164a7a" stroke-width="5"/></svg>
    <div class="abs" style="left:130px;top:55px;width:165px">
      <div class="quiz-title">Try the<br>lorvikometer!</div>
      <p class="quiz-text">Are you working entrepreneurship like?</p>
    </div>
    <a class="btn" style="left:130px;top:152px;width:132px" href="#">START QUIZ<span class="go"></span></a>
  </section>

  <section class="abs panel" style="left:495px;top:518px;width:624px;height:205px">
    <div class="panel-head" style="padding-left:19px">Get started!</div>
    <div class="abs list-col" style="left:21px;top:40px">
      <h3>Teaching plans</h3>
      <ul><li>» Lorem ipsum dolor sit amet</li><li>» Onsectetur adipiscing elit</li><li>» Onsectetur</li><li>» Adipiscing elit dolor sit</li><li>» Dolor sit lorem ipsum.</li></ul>
    </div>
    <div class="abs" style="left:311px;top:48px;height:145px;border-left:1px solid #b9cfe3"></div>
    <div class="abs list-col" style="left:341px;top:40px">
      <h3>Methods</h3>
      <ul><li class="active">» Café-pedagogikk</li><li>» Elevbedrift</li><li>» Gründercamp</li><li>» Story line</li><li>» Real</li></ul>
    </div>
  </section>

  <section class="abs panel" style="left:170px;top:748px;width:950px;height:245px">
    <div class="panel-head">Get Inspired!</div>
    <article class="card" style="left:23px">
      <div class="thumb" role="img" aria-label="Photo of a student carrying a stack of books in a library" style="background:linear-gradient(135deg,#e8c9a0,#f1ede6 50%,#b8c4cc)"></div>
      <div class="body"><h4>Lorem ipsum dolor sit amet</h4><p>Onsectetur adipiscing elit. Onsectetur elit dolor onsectetur adipiscing elit, sectetur adipiscing dolor elit</p><div class="more">» Read more</div></div>
    </article>
    <article class="card" style="left:339px">
      <div class="thumb" role="img" aria-label="Photo of students writing at their desks" style="background:linear-gradient(135deg,#6d4f3c,#d8c0a0 50%,#e8e2da)"></div>
      <div class="body"><h4>Lorem ipsum dolor sit amet</h4><p>Onsectetur adipiscing elit. Onsectetur elit dolor onsectetur adipiscing elit, sectetur adipiscing dolor elit</p><div class="more">» Read more</div></div>
    </article>
    <article class="card" style="left:651px">
      <div class="thumb" role="img" aria-label="Photo of a student concentrating on written work" style="background:linear-gradient(135deg,#8a5a3e,#e8ddd2 55%,#f4f2f0)"></div>
      <div class="body"><h4>Lorem ipsum dolor sit amet</h4><p>Onsectetur adipiscing elit. Onsectetur elit dolor onsectetur adipiscing elit, sectetur adipiscing dolor elit</p><div class="more">» Read more</div></div>
    </article>
  </section>
  <div class="abs arrow" style="left:150px;background:var(--blue)">‹</div>
  <div class="abs arrow" style="left:1120px;background:var(--pink)">›</div>
  <div class="abs pager"><span></span><span></span><span class="on"></span><span></span></div>

  <footer class="abs footer">
    <div class="abs f-brand"><span class="dot"></span>Lorvik</div>
    <div class="rule"></div>
    <p class="abs copy">All rights reserved | Lorvik.no 2012</p>
    <h5 style="left:489px;top:30px">Pedagogical<br>entrepreneurship</h5>
    <ul style="left:489px"><li>» What is Pedagogical entrepreneurship?</li><li>» Science</li><li>» Best practice schools</li><li>» Lorvikometer</li><li>» About lorvik.no</li></ul>
    <h5 style="left:768px;top:54px">Methods</h5>
    <ul style="left:768px"><li class="hot">» Story line</li><li>» Real</li><li>» Café-pedagogikk</li><li>» Blabla</li></ul>
    <h5 style="left:949px;top:54px">Teaching plans</h5>
    <ul style="left:949px"><li>» Lorem ipsum</li><li>» Dolor sit amet</li><li>» Onsectetur</li><li>» Adipiscing elit</li></ul>
  </footer>
</div>
</body>
</html>
```